Letterhead Design for Higher Education provider

Company Name: PVRA Credentials
Motto: Quality in Learning
Address: Kelmont House, Harrier Lane, Fernbrook Trade Park, Dartford DA4 2RX, United Kingdom
T: +44 (0)20 7946 0582
E: info@pvra-example.org.uk
W: www.pvra-example.org.uk
Legal information: PVRA Credentials is incorporated in England & Wales | Company Reg. No. 07315428

Target Market(s)

Higher Education provider

Industry/Entity Type

Education

Font styles to use
Sans Serif

Requirements
Must have
• Company Name, Address, tel, email, web, company legal information.
Nice to have
• motto
Should not have
• should not cover to much of printing areas

```html
<!DOCTYPE html>
<html lang="en">
<head>
<meta charset="utf-8">
<title>PVRA Credentials Letterhead</title>
<link rel="stylesheet" href="https://fonts.googleapis.com/css2?family=Noto+Sans:wght@400&family=PT+Sans+Narrow&display=swap">
<style>
  :root {
    --brand-navy: #2b3a74;
    --motto-fill: #9795bc;
    --motto-ink: #2b2762;
    --paper: #ffffff;
    --ink: #111111;
    --rule: #000000;
  }
  * { margin: 0; padding: 0; box-sizing: border-box; }
  html, body { width: 927px; height: 1200px; overflow: hidden; background: var(--paper); }
  .letterhead {
    position: relative;
    width: 927px;
    height: 1200px;
    background: var(--paper);
    font-family: "Noto Sans", sans-serif;
    overflow: hidden;
  }
  .header-wave { position: absolute; left: 0; top: 0; width: 927px; height: 190px; }
  .reg-number {
    position: absolute;
    left: 29px; top: 36px;
    width: 219px;
    padding-bottom: 4px;
    border-bottom: 3px solid var(--paper);
    font-family: "PT Sans Narrow", sans-serif;
    font-size: 18px;
    color: var(--paper);
    text-align: center;
    letter-spacing: 0.2px;
  }
  .motto {
    position: absolute;
    left: 305px; top: 38px;
    width: 272px; height: 32px;
    border-radius: 14px;
    background: var(--motto-fill);
    color: var(--motto-ink);
    font-size: 26px;
    line-height: 32px;
    text-align: center;
    letter-spacing: 0.3px;
  }
  .brand-name {
    position: absolute;
    right: 44px; top: 38px;
    color: var(--paper);
    font-size: 56px;
    line-height: 1;
    letter-spacing: 1px;
  }
  .footer-band {
    position: absolute;
    left: 0; top: 1067px;
    width: 927px; height: 98px;
    background: var(--brand-navy);
    color: var(--paper);
  }
  .address {
    position: absolute;
    left: 14px; top: 17px;
    width: 340px;
    font-size: 17.5px;
    line-height: 22px;
    text-align: center;
    letter-spacing: 0.4px;
  }
  .contacts {
    position: absolute;
    right: 18px; top: 6px;
    list-style: none;
  }
  .contacts li {
    display: flex;
    justify-content: flex-end;
    align-items: center;
    height: 23px;
    font-size: 16.5px;
    letter-spacing: 0.2px;
  }
  .contacts .icon { width: 14px; height: 14px; margin-left: 14px; fill: var(--paper); }
  .legal-line {
    position: absolute;
    left: 0; top: 1170px;
    width: 927px;
    font-size: 17.5px;
    color: var(--ink);
    text-align: center;
    letter-spacing: 0.4px;
  }
</style>
</head>
<body>
<main class="letterhead">
  <svg class="header-wave" viewBox="0 0 927 190" aria-hidden="true">
    <path d="M0,0 H927 V186 C770,124 420,92 0,94 Z" fill="var(--brand-navy)"/>
    <path d="M0,94 C420,92 770,124 927,186" fill="none" stroke="var(--rule)" stroke-width="1"/>
  </svg>

  <div class="reg-number">Company Reg. No. 07315428</div>
  <div class="motto">Quality in Learning</div>
  <div class="brand-name">pvra</div>

  <footer class="footer-band">
    <address class="address" style="font-style:normal">
      Address : Kelmont House, Harrier Lane,<br>
      Fernbrook Trade Park,<br>
      Dartford DA4 2RX, United Kingdom
    </address>
    <ul class="contacts">
      <li>+44(0)77 0090 3168
        <svg class="icon" viewBox="0 0 14 14" aria-hidden="true"><path d="M3.5,0.5 h7 a1,1 0 0 1 1,1 v11 a1,1 0 0 1 -1,1 h-7 a1,1 0 0 1 -1,-1 v-11 a1,1 0 0 1 1,-1 Z M4.5,2 v8 h5 v-8 Z M7,11 a0.8,0.8 0 1 0 0.01,0 Z" fill-rule="evenodd"/></svg>
      </li>
      <li>+44(0)20 7946 0582
        <svg class="icon" viewBox="0 0 14 14" aria-hidden="true"><path d="M0.5,5 C2,1.5 12,1.5 13.5,5 L11,6 L10,4.5 H4 L3,6 Z M3,7 H11 L12.5,12.5 H1.5 Z"/></svg>
      </li>
      <li>admissions@pvra-example.org.uk
        <svg class="icon" viewBox="0 0 14 14" aria-hidden="true"><path d="M0.5,3 H13.5 V11.5 H0.5 Z M1.5,4 L7,8 L12.5,4 M1.5,10.5 L5.5,7 M12.5,10.5 L8.5,7" fill="none" stroke="var(--paper)" stroke-width="1.2"/></svg>
      </li>
      <li>www.pvra-example.org.uk
        <svg class="icon" viewBox="0 0 14 14" aria-hidden="true"><g fill="none" stroke="var(--paper)" stroke-width="1.1"><circle cx="7" cy="7" r="6"/><ellipse cx="7" cy="7" rx="2.6" ry="6"/><path d="M1,7 H13 M2,4 H12 M2,10 H12"/></g></svg>
      </li>
    </ul>
  </footer>

  <p class="legal-line">Legal information: PVRA Credentials is incorporated in England &amp; Wales</p>
</main>
</body>
</html>
```